Brookvale Insurance Services - Insurance Agency Wesbite

I need a website for my insurance agency called Brookvale Insurance Services. I have attached my company logo. You can use the colors from the copy logo to create the website color scheme. I need a Request A Quote section.
Business Address: 7816 Marlowe Ave Unit D, Studio City Ca 91627
Business Phone: (818) 555-0193
I would need the following drop downs on the main page:

1st drop down:
Business Insurance
⁃ Commercial Auto
⁃ Employment Practice Liability Insurance
⁃ General Liability Insurance
⁃ Professional Liability Insurance
⁃ Property Insurance
⁃ Workers Compensation Insurance

2nd drop down:
Industries We Serve
- Construction
- Janitorial
- Landscapers
- Trucking
- ParcelRun Independent Service Providers (ISP)
Healthcare Industry
- Community Care Facilities
- Home Health Agencies
- Hospice
- Nursing Homes

3rd drop down:
Risk Management
- Claims Management
- Compliance & Risk Management

4th drop down
Request a quote

5th drop down
About Us

6th drop down
Contact US

Target Market(s)

Potential clients

Industry/Entity Type

Business Insurance

Coding

Coded - Design and coding required

Number of Pages Required

5+ page

Colors
0054AA
0677BA
7BADD7
CADEEF
E8F1F8
00AB8E
00BBA5
67D7C9
C6EFE9
E9F9F6

Requirements
Must have
• Home Business Insurance - Commercial Auto - Employment Practice Liability Insurance - General Liability Insurance - Professional Liability Insurance - Property Insurance - Workers Compensation Insurance Industries We Serve - Construction - Janitorial - Landscapers - Manufacturing Companies - Restaurants - Towing - Trucking Healthcare Industry - Community Care Facilities - Home Health Agencies - Hospice - Nursing Homes - Risk Management - Claims Management - Compliance & Risk Management Request a Quote About Us Contact Us

```html
<!DOCTYPE html>
<html lang="en">
<head>
<meta charset="utf-8">
<title>Brookvale Insurance Services</title>
<link href="https://fonts.googleapis.com/css2?family=Poppins:wght@400;500;600;700;800&display=swap" rel="stylesheet">
<style>
:root{
  --navy:#0b1f5e;
  --navy-deep:#0d2348;
  --navy-bar:#1b3a62;
  --ink:#1d3466;
  --text:#1f2a3d;
  --blue:#0054aa;
  --blue-mid:#2f6fb8;
  --green:#00ab8e;
  --green-deep:#009477;
  --mint:#e9f9f6;
  --mint-card:#e3f8f3;
  --sky:#edf3fb;
  --red:#e0383b;
  --white:#ffffff;
}
*{box-sizing:border-box;margin:0;padding:0}
html,body{width:1200px;height:5002px;overflow:hidden}
body{position:relative;font-family:"Poppins",sans-serif;color:var(--text);background:var(--white)}
.abs{position:absolute}
a{color:inherit;text-decoration:none}
.btn{position:absolute;display:flex;align-items:center;justify-content:center;background:var(--green);color:var(--white);font-size:13px;font-weight:500;border-radius:4px}
.learn{display:flex;align-items:center;gap:8px;color:var(--green);font-size:12.5px;font-weight:500;margin-top:6px}
.section-title{position:absolute;left:0;width:1200px;text-align:center;font-size:38px;font-weight:500;color:var(--ink)}

/* header */
.header{top:0;left:0;width:1200px;height:82px;background:#fff}
.brand{position:absolute;left:173px;top:24px;font-size:21px;font-weight:600;color:var(--blue);line-height:1.05;width:230px}
.brand small{display:block;font-size:21px;font-weight:600}
.nav{top:82px;left:0;width:1200px;height:50px;background:var(--navy)}
.nav ul{list-style:none;display:flex;gap:17px;position:absolute;left:173px;top:16px}
.nav li{color:#fff;font-size:12.5px;font-weight:500}

/* hero */
.hero{top:132px;left:0;width:1200px;height:560px;background:linear-gradient(100deg,#d7e5ee 0%,#a9bfd0 40%,#e9eff3 70%,#b8c4cc 100%)}
.hero h1{position:absolute;left:173px;top:92px;font-size:43px;line-height:62px;font-weight:800;color:var(--navy)}
.hero p{position:absolute;left:173px;top:228px;width:500px;font-size:13px;line-height:24px;color:#111;font-weight:500}

/* business */
.bi-item{position:absolute;width:240px}
.bi-head{display:flex;align-items:center;gap:12px;font-size:13px;font-weight:500;color:var(--text);line-height:20px}
.icon-box{width:56px;height:56px;border-radius:6px;background:var(--green);display:flex;align-items:center;justify-content:center;flex:none}
.bi-item p{font-size:12px;line-height:20px;margin-top:12px;color:#222}
.center-figure{left:437px;top:872px;width:312px;height:200px;background:radial-gradient(circle at 50% 40%,#d9c3ae 0,#a6b6c9 35%,#fff 72%)}
.logo-card{left:452px;top:1097px;width:301px;height:140px;background:#fff;border-radius:6px;box-shadow:0 4px 16px rgba(0,0,0,.15);display:flex;align-items:center;justify-content:center;text-align:center;font-size:24px;font-weight:600;color:var(--blue);line-height:1.2}

/* industries */
.ind-title{left:175px;top:1470px;color:#fff;font-size:38px;font-weight:500;line-height:58px}
.ind-text{left:175px;top:1596px;width:260px;color:#fff;font-size:12px;line-height:19px}
.card{position:absolute;width:276px;height:310px;background:#fff;border-radius:4px;padding:6px}
.card .photo{height:190px;border-radius:2px;position:relative}
.card .badge{position:absolute;left:6px;bottom:-4px;width:30px;height:30px;background:#fff;border-radius:4px;display:flex;align-items:center;justify-content:center}
.card h3{font-size:13px;font-weight:500;margin:14px 8px 4px}
.card p{font-size:12px;line-height:19px;color:#555;margin:0 8px}
.card .learn{margin:6px 8px 0}

/* healthcare */
.hc-card{position:absolute;top:2466px;width:203px;height:117px;background:var(--mint-card);text-align:center;font-size:16px;font-weight:500;color:var(--ink);line-height:21px;display:flex;align-items:flex-end;justify-content:center;padding-bottom:16px}
.hc-ring{position:absolute;top:-40px;left:61px;width:80px;height:80px;border-radius:50%;background:#bfeee3;display:flex;align-items:center;justify-content:center}
.hc-ring span{width:62px;height:62px;border-radius:50%;background:var(--green);display:flex;align-items:center;justify-content:center;border:4px solid #fff}

/* risk */
.col-head{position:absolute;top:2890px;font-size:19px;font-weight:600;color:#15203a}
.row{position:absolute;width:420px;height:38px;background:#fff;display:flex;align-items:center;gap:10px;padding-left:10px;font-size:13.5px;font-weight:500;color:#1c2440;box-shadow:0 1px 4px rgba(0,0,0,.05)}
.dot{width:16px;height:16px;border-radius:50%;display:flex;align-items:center;justify-content:center;flex:none}

/* about */
.about-photo{left:173px;top:3395px;width:408px;height:407px;background:linear-gradient(135deg,#4a4a4a,#8b8f95 45%,#c9c4bd 70%,#5c6066)}
.about h2{position:absolute;left:608px;top:3455px;font-size:38px;font-weight:500;color:var(--ink)}
.about p{position:absolute;left:608px;top:3528px;width:408px;font-size:12px;line-height:21px;color:#333}

/* contact */
.contact-card{left:173px;top:4000px;width:419px;height:476px;background:var(--green-deep);color:#fff;padding:42px 30px}
.contact-card h2{font-size:38px;font-weight:500}
.contact-card .lead{font-size:12px;line-height:20px;margin:14px 0 0 6px;width:340px}
.c-item{position:absolute;left:37px;display:flex;gap:14px}
.c-icon{width:48px;height:48px;background:#fff;border-radius:4px;display:flex;align-items:center;justify-content:center;flex:none}
.c-item b{display:block;font-size:16px;font-weight:600}
.c-item span{font-size:12px}
.quote h2{position:absolute;left:656px;top:3995px;font-size:38px;font-weight:500;color:var(--ink)}
.field{position:absolute;left:656px;width:371px;border-bottom:1px solid #9cb6d9;padding-bottom:8px}
.field label{display:block;font-size:15px;font-weight:500;color:var(--ink)}
.field span{display:block;font-size:12px;color:#a4adbb;margin-top:4px}

/* footer */
.foot-logo{left:0;top:4685px;width:1200px;text-align:center;color:#fff;font-size:40px;font-weight:600;line-height:1.15}
.foot-nav{left:0;top:4790px;width:1200px;display:flex;justify-content:center;gap:18px;color:#fff;font-size:12.5px;list-style:none}
.socials{left:0;top:4853px;width:1200px;display:flex;justify-content:center;gap:18px}
.socials span{width:30px;height:30px;border-radius:50%;background:#fff}
.bottom-bar{left:0;top:4938px;width:1200px;height:64px;background:var(--navy-bar);color:#d5deea;font-size:12px}
</style>
</head>
<body>

<header class="abs header">
  <div class="brand">Brookvale<small>Insurance Services</small></div>
  <a class="btn" style="left:856px;top:19px;width:171px;height:41px">Request a quote</a>
</header>
<nav class="abs nav">
  <ul>
    <li>Business Insurance</li><li>Industries We Serve</li><li>Healthcare Industry</li><li>Risk Management</li><li>Request a quote</li><li>About Us</li><li>Contact US</li>
  </ul>
</nav>

<section class="abs hero" role="img" aria-label="Businessman standing on a rocky summit above a city skyline">
  <h1>Business To Risky ?<br>We’ll Take Care of That!</h1>
  <p>Lorem ipsum dolor sit amet, consectetur adipiscing elit, sed do eiusmod tempor incididunt ut labore et dolore magna aliqua. Ut enim ad minim veniam, quis nostrud exercitation ullamco laboris</p>
  <a class="btn" style="left:0;top:320px;margin-left:173px;width:173px;height:42px">Request a quote</a>
</section>
<svg class="abs" style="left:0;top:600px" width="1200" height="100" viewBox="0 0 1200 100">
  <polygon points="0,92 369,22 1200,70 1200,100 0,100" fill="var(--green)"/>
  <polygon points="0,98 369,34 1200,82 1200,100 0,100" fill="#fff"/>
</svg>

<!-- Business insurance -->
<h2 class="section-title" style="top:762px">Business Insurance</h2>

<div class="bi-item" style="left:173px;top:835px">
  <div class="bi-head"><span class="icon-box"><svg width="30" height="30" viewBox="0 0 24 24" fill="none" stroke="#fff" stroke-width="1.6"><path d="M4 15l2-6h12l2 6v4H4z"/><circle cx="8" cy="17" r="1.5"/><circle cx="16" cy="17" r="1.5"/></svg></span>Commercial Auto</div>
  <p>Lorem ipsum dolor sit amet, consectetur adipiscing elit, sed do</p>
  <a class="learn">Learn More <span>→</span></a>
</div>
<div class="bi-item" style="left:173px;top:990px">
  <div class="bi-head"><span class="icon-box"><svg width="30" height="30" viewBox="0 0 24 24" fill="none" stroke="#fff" stroke-width="1.6"><circle cx="8" cy="8" r="2.5"/><circle cx="16" cy="8" r="2.5"/><path d="M3 20c0-4 3-6 5-6s5 2 5 6M11 20c0-4 3-6 5-6s5 2 5 6"/></svg></span>Employment Practice<br>Liability Insurance</div>
  <p>Lorem ipsum dolor sit amet, consectetur adipiscing elit, sed do</p>
  <a class="learn">Learn More <span>→</span></a>
</div>
<div class="bi-item" style="left:173px;top:1144px">
  <div class="bi-head"><span class="icon-box"><svg width="30" height="30" viewBox="0 0 24 24" fill="none" stroke="#fff" stroke-width="1.6"><path d="M3 11a9 9 0 0118 0z"/><path d="M12 11v8a2 2 0 01-4 0"/></svg></span>General<br>Liability Insurance</div>
  <p>Lorem ipsum dolor sit amet, consectetur adipiscing elit, sed do</p>
  <a class="learn">Learn More <span>→</span></a>
</div>

<div class="abs center-figure" role="img" aria-label="Relaxed businessman meditating at a desk with a laptop"></div>
<div class="abs logo-card">Brookvale<br>Insurance Services</div>

<div class="bi-item" style="left:812px;top:835px">
  <div class="bi-head"><span class="icon-box"><svg width="30" height="30" viewBox="0 0 24 24" fill="none" stroke="#fff" stroke-width="1.6"><circle cx="12" cy="6" r="3"/><path d="M6 21v-5a6 6 0 0112 0v5z"/></svg></span>Professional<br>Liability Insurance</div>
  <p>Lorem ipsum dolor sit amet, consectetur adipiscing elit, sed do</p>
  <a class="learn">Learn More <span>→</span></a>
</div>
<div class="bi-item" style="left:812px;top:990px">
  <div class="bi-head"><span class="icon-box"><svg width="30" height="30" viewBox="0 0 24 24" fill="none" stroke="#fff" stroke-width="1.6"><path d="M3 11l9-7 9 7"/><path d="M5 10v10h14V10"/><path d="M10 20v-5h4v5"/></svg></span>Property<br>Insurance</div>
  <p>Lorem ipsum dolor sit amet, consectetur adipiscing elit, sed do</p>
  <a class="learn">Learn More <span>→</span></a>
</div>
<div class="bi-item" style="left:812px;top:1144px">
  <div class="bi-head"><span class="icon-box"><svg width="30" height="30" viewBox="0 0 24 24" fill="none" stroke="#fff" stroke-width="1.6"><path d="M12 3l8 3v6c0 5-4 8-8 9-4-1-8-4-8-9V6z"/><circle cx="12" cy="10" r="2.5"/><path d="M8 17c1-2 2.5-3 4-3s3 1 4 3"/></svg></span>Workers<br>Compensation<br>Insurance</div>
  <p>Lorem ipsum dolor sit amet, consectetur adipiscing elit, sed do</p>
  <a class="learn">Learn More <span>→</span></a>
</div>

<!-- Industries -->
<svg class="abs" style="left:0;top:1325px" width="1200" height="980" viewBox="0 0 1200 980">
  <polygon points="130,77 855,3 1200,77" fill="var(--blue-mid)"/>
  <polygon points="0,79 855,18 1200,79 1200,975 0,975" fill="var(--navy)"/>
  <polygon points="0,975 0,975 295,890 1200,962 1200,980 0,980" fill="var(--blue-mid)"/>
  <polygon points="0,980 0,968 295,902 1200,975 1200,980" fill="#fff"/>
</svg>
<h2 class="abs ind-title">Industries<br>We Serve</h2>
<p class="abs ind-text">Lorem ipsum dolor sit amet, consectetur adipiscing elit, sed do eiusmod tempor incididunt ut labore et dolore magna.</p>
<a class="btn" style="left:175px;top:1682px;width:172px;height:40px">Request a quote</a>

<div class="card" style="left:462px;top:1480px">
  <div class="photo" role="img" aria-label="Construction site with workers and crane" style="background:linear-gradient(180deg,#6fa6e0,#b6c9d8 55%,#7a7166)"><span class="badge"><svg width="18" height="18" viewBox="0 0 24 24" fill="none" stroke="var(--blue)" stroke-width="1.8"><path d="M4 14a8 8 0 0116 0zM3 18h18"/></svg></span></div>
  <h3>Construction</h3><p>Lorem ipsum dolor sit amet, consectetur adipiscing elit, sed do</p><a class="learn">Learn More <span>→</span></a>
</div>
<div class="card" style="left:753px;top:1480px">
  <div class="photo" role="img" aria-label="Janitorial staff cleaning an office" style="background:linear-gradient(180deg,#e8ecef,#c7ced6 60%,#7f8fa6)"><span class="badge"><svg width="18" height="18" viewBox="0 0 24 24" fill="none" stroke="var(--blue)" stroke-width="1.8"><path d="M12 3v10M7 21l2-8h6l2 8z"/></svg></span></div>
  <h3>Janitorial</h3><p>Lorem ipsum dolor sit amet, consectetur adipiscing elit, sed do</p><a class="learn">Learn More <span>→</span></a>
</div>
<div class="card" style="left:175px;top:1820px">
  <div class="photo" role="img" aria-label="Landscaper mowing a lawn beside a gazebo" style="background:linear-gradient(180deg,#8aa36a,#4f7a3a 55%,#6aa44a)"><span class="badge"><svg width="18" height="18" viewBox="0 0 24 24" fill="none" stroke="var(--blue)" stroke-width="1.8"><path d="M4 20c4-2 12-2 16 0M8 18V9M12 18V6M16 18V9"/></svg></span></div>
  <h3>Landscapers</h3><p>Lorem ipsum dolor sit amet, consectetur adipiscing elit, sed do</p><a class="learn">Learn More <span>→</span></a>
</div>
<div class="card" style="left:462px;top:1820px">
  <div class="photo" role="img" aria-label="Workers in safety vests beside trucks and containers" style="background:linear-gradient(180deg,#c9d3dd,#8d99a8 50%,#6b6f73)"><span class="badge"><svg width="18" height="18" viewBox="0 0 24 24" fill="none" stroke="var(--blue)" stroke-width="1.8"><path d="M2 7h12v9H2zM14 10h4l3 3v3h-7z"/><circle cx="6" cy="18" r="1.5"/><circle cx="17" cy="18" r="1.5"/></svg></span></div>
  <h3>Trucking</h3><p>Lorem ipsum dolor sit amet, consectetur adipiscing elit, sed do</p><a class="learn">Learn More <span>→</span></a>
</div>
<div class="card" style="left:753px;top:1820px">
  <div class="photo" role="img" aria-label="Delivery worker holding a parcel among boxes" style="background:linear-gradient(160deg,#d8b98e,#c58a4d 50%,#e46b2a)"><span class="badge"><svg width="18" height="18" viewBox="0 0 24 24" fill="none" stroke="var(--blue)" stroke-width="1.8"><path d="M4 8l8-4 8 4v8l-8 4-8-4zM4 8l8 4 8-4M12 12v8"/></svg></span></div>
  <h3>ParcelRun Independent (ISP)</h3><p>Lorem ipsum dolor sit amet, consectetur adipiscing elit, sed do</p><a class="learn">Learn More <span>→</span></a>
</div>

<!-- Healthcare -->
<h2 class="section-title" style="top:2340px">Healthcare Industry</h2>
<div class="hc-card" style="left:173px"><div class="hc-ring"><span><svg width="28" height="28" viewBox="0 0 24 24" fill="none" stroke="#fff" stroke-width="1.7"><circle cx="8" cy="8" r="2.5"/><circle cx="16" cy="8" r="2.5"/><path d="M3 20c0-4 2-6 5-6s5 2 5 6M11 20c0-4 2-6 5-6s5 2 5 6"/></svg></span></div>Community<br>Care Facilities</div>
<div class="hc-card" style="left:391px"><div class="hc-ring"><span><svg width="28" height="28" viewBox="0 0 24 24" fill="none" stroke="#fff" stroke-width="1.7"><path d="M3 11l9-7 9 7v9H3z"/><path d="M12 10v6M9 13h6"/></svg></span></div>Home Health<br>Agencies</div>
<div class="hc-card" style="left:609px;padding-bottom:26px"><div class="hc-ring"><span><svg width="28" height="28" viewBox="0 0 24 24" fill="none" stroke="#fff" stroke-width="1.7"><circle cx="12" cy="5" r="2"/><path d="M12 8v6l-4 6M12 14l4 6M7 11h10"/></svg></span></div>Hospice</div>
<div class="hc-card" style="left:826px"><div class="hc-ring"><span><svg width="28" height="28" viewBox="0 0 24 24" fill="none" stroke="#fff" stroke-width="1.7"><circle cx="12" cy="8" r="3.5"/><path d="M5 21c0-4 3-7 7-7s7 3 7 7"/><path d="M12 14v4M10 16h4"/></svg></span></div>Nursing<br>Homes</div>

<!-- Risk management -->
<svg class="abs" style="left:0;top:2670px" width="1200" height="705" viewBox="0 0 1200 705">
  <polygon points="155,88 860,6 1170,88" fill="var(--green)"/>
  <polygon points="0,90 860,22 1200,90 1200,705 0,705" fill="var(--mint)"/>
  <polygon points="0,700 340,600 1200,692 1200,705 0,705" fill="var(--green)"/>
  <polygon points="0,705 340,616 1200,703 1200,705" fill="#fff"/>
</svg>
<h2 class="section-title" style="top:2795px">Risk Management</h2>
<h3 class="col-head" style="left:173px">Claims Management</h3>
<h3 class="col-head" style="left:610px">Compliance &amp; Risk Management</h3>

<div class="row" style="left:173px;top:2943px"><span class="dot" style="background:var(--green)"><svg width="10" height="10" viewBox="0 0 10 10"><path d="M2 5l2 2 4-4" stroke="#fff" stroke-width="1.6" fill="none"/></svg></span>Lorem ipsum dolor sit amet,consectetur adipiscing.</div>
<div class="row" style="left:173px;top:2993px"><span class="dot" style="background:var(--green)"><svg width="10" height="10" viewBox="0 0 10 10"><path d="M2 5l2 2 4-4" stroke="#fff" stroke-width="1.6" fill="none"/></svg></span>Lorem ipsum dolor sit amet,consectetur adipiscing.</div>
<div class="row" style="left:173px;top:3043px"><span class="dot" style="background:var(--green)"><svg width="10" height="10" viewBox="0 0 10 10"><path d="M2 5l2 2 4-4" stroke="#fff" stroke-width="1.6" fill="none"/></svg></span>Lorem ipsum dolor sit amet,consectetur adipiscing.</div>
<div class="row" style="left:173px;top:3093px"><span class="dot" style="background:var(--green)"><svg width="10" height="10" viewBox="0 0 10 10"><path d="M2 5l2 2 4-4" stroke="#fff" stroke-width="1.6" fill="none"/></svg></span>Lorem ipsum dolor sit amet,consectetur adipiscing.</div>
<div class="row" style="left:173px;top:3143px"><span class="dot" style="background:var(--green)"><svg width="10" height="10" viewBox="0 0 10 10"><path d="M2 5l2 2 4-4" stroke="#fff" stroke-width="1.6" fill="none"/></svg></span>Lorem ipsum dolor sit amet,consectetur adipiscing.</div>

<div class="row" style="left:608px;top:2943px"><span class="dot" style="background:var(--red)"><svg width="10" height="10" viewBox="0 0 10 10"><path d="M3 3l4 4M7 3l-4 4" stroke="#fff" stroke-width="1.6"/></svg></span>Lorem ipsum dolor sit amet,consectetur adipiscing.</div>
<div class="row" style="left:608px;top:2993px"><span class="dot" style="background:var(--red)"><svg width="10" height="10" viewBox="0 0 10 10"><path d="M3 3l4 4M7 3l-4 4" stroke="#fff" stroke-width="1.6"/></svg></span>Lorem ipsum dolor sit amet,consectetur adipiscing.</div>
<div class="row" style="left:608px;top:3043px"><span class="dot" style="background:var(--red)"><svg width="10" height="10" viewBox="0 0 10 10"><path d="M3 3l4 4M7 3l-4 4" stroke="#fff" stroke-width="1.6"/></svg></span>Lorem ipsum dolor sit amet,consectetur adipiscing.</div>
<div class="row" style="left:608px;top:3093px"><span class="dot" style="background:var(--red)"><svg width="10" height="10" viewBox="0 0 10 10"><path d="M3 3l4 4M7 3l-4 4" stroke="#fff" stroke-width="1.6"/></svg></span>Lorem ipsum dolor sit amet,consectetur adipiscing.</div>
<div class="row" style="left:608px;top:3143px"><span class="dot" style="background:var(--red)"><svg width="10" height="10" viewBox="0 0 10 10"><path d="M3 3l4 4M7 3l-4 4" stroke="#fff" stroke-width="1.6"/></svg></span>Lorem ipsum dolor sit amet,consectetur adipiscing.</div>

<!-- About -->
<section class="about">
  <svg class="abs" style="left:500px;top:3760px" width="90" height="70" viewBox="0 0 90 70"><polygon points="0,42 81,0 81,60 72,70 72,42" fill="var(--green)"/></svg>
  <div class="abs about-photo" role="img" aria-label="Three colleagues reviewing work on a laptop"></div>
  <h2>About Us</h2>
  <p>Lorem ipsum dolor sit amet, consectetur adipiscing elit, sed do eiusmod tempor incididunt ut labore et dolore magna aliqua. Ut enim ad minim veniam, quis nostrud exercitation ullamco laboris nisi ut aliquip ex ea commodo consequat. Duis aute irure dolor in reprehenderit in voluptate velit esse cillum dolore eu fugiat nulla pariatur. Excepteur sint occaecat cupidatat non proident, sunt in culpa qui officia deserunt mollit anim id est laborum.</p>
  <a class="btn" style="left:608px;top:3700px;width:144px;height:41px">Learn More</a>
</section>

<!-- Contact -->
<svg class="abs" style="left:0;top:3860px" width="1200" height="820" viewBox="0 0 1200 820">
  <polygon points="155,83 855,5 1175,83" fill="var(--blue-mid)"/>
  <polygon points="0,85 855,20 1200,85 1200,820 0,820" fill="var(--sky)"/>
  <polygon points="0,740 340,690 1200,800 1200,820 0,820" fill="var(--blue-mid)"/>
  <polygon points="0,752 340,704 1200,812 1200,820 0,820" fill="var(--navy-deep)"/>
</svg>
<div class="abs" style="left:0;top:4678px;width:1200px;height:260px;background:var(--navy-deep)"></div>

<section class="abs contact-card">
  <h2>Contact Us</h2>
  <p class="lead">We always get back to you within a maximum of 24 hours. You are of course also welcome to call us.</p>
  <div class="c-item" style="top:180px"><span class="c-icon"><svg width="22" height="22" viewBox="0 0 24 24" fill="var(--green-deep)"><path d="M12 2a7 7 0 00-7 7c0 5 7 13 7 13s7-8 7-13a7 7 0 00-7-7zm0 9.5A2.5 2.5 0 1112 6.5a2.5 2.5 0 010 5z"/></svg></span><div><b>Address:</b><span>7816 Marlowe Ave Unit D, Studio City Ca 91627</span></div></div>
  <div class="c-item" style="top:275px"><span class="c-icon"><svg width="22" height="22" viewBox="0 0 24 24" fill="var(--green-deep)"><path d="M6.6 10.8a15 15 0 006.6 6.6l2.2-2.2a1 1 0 011-.25 11 11 0 003.6.6 1 1 0 011 1V20a1 1 0 01-1 1A17 17 0 013 4a1 1 0 011-1h3.5a1 1 0 011 1 11 11 0 00.6 3.6 1 1 0 01-.25 1z"/></svg></span><div><b>Telephone:</b><span>(818) 555-0193</span></div></div>
  <div class="c-item" style="top:370px"><span class="c-icon"><svg width="22" height="22" viewBox="0 0 24 24" fill="var(--green-deep)"><path d="M3 5h18v14H3z"/><path d="M3 6l9 7 9-7" stroke="#fff" stroke-width="1.6" fill="none"/></svg></span><div><b>E-mail:</b><span>info@brookvaleins.com</span></div></div>
</section>

<section class="quote">
  <h2>Request a Quote</h2>
  <div class="field" style="top:4100px"><label>Name</label><span>John Doe</span></div>
  <div class="field" style="top:4186px"><label>Email</label><span>info@brookvaleins.com</span></div>
  <div class="field" style="top:4272px"><label>Phone</label><span>+91 1234567890</span></div>
  <div class="field" style="top:4374px"><label>Message</label><span>Write your message......</span></div>
  <a class="btn" style="left:656px;top:4451px;width:123px;height:36px;font-size:12px">SUBMIT</a>
</section>

<!-- Footer -->
<div class="abs foot-logo">Brookvale<br><span style="font-size:18px;letter-spacing:4px">Insurance Services</span></div>
<ul class="abs foot-nav"><li>Business Insurance</li><li>Industries We Serve</li><li>Healthcare Industry</li><li>Risk Management</li><li>Request A Quote</li><li>About Us</li><li>Contact US</li></ul>
<div class="abs socials"><span></span><span></span><span></span></div>
<footer class="abs bottom-bar">
  <span class="abs" style="left:168px;top:25px">All content © Copyright 2024 <b style="color:#fff;font-weight:600">Brookvale</b>. All rights reserved.</span>
  <span class="abs" style="left:867px;top:25px">Privacy policy</span>
  <span class="abs" style="left:969px;top:25px">Cookies</span>
</footer>

</body>
</html>
```